"Life's Short. Get a Divorce" - WANTED - Simple, Classy & Sexy Poster!

I am looking for a racy, lacy, sexy, jaw dropping poster to be created that has a picture of a good looking man and woman on either side of the poster which has the slogan 'Life's short. Get a Divorce'. I would also like our company's contact details (along with the services that we offer) to be included in the flyer.

In relation to the images, we would like that show only the bodies of a muscular man and a leggy woman in high heels.

If we could have the woman on one side and the man on the other side (so 2 separate images) with the 'Life's Short. Get a Divorce' in the centre of the page.

Target Market(s)

Mature audience

Requirements
Must have
• A picture of a mature man and woman.
• The slogan 'Life's Short. Get a Divorce' in large bold font.
• Company's header and footer.

```html
<!DOCTYPE html>
<html lang="en">
<head>
<meta charset="utf-8">
<title>Marlow Keane Legal – Life's Short</title>
<link rel="stylesheet" href="https://fonts.googleapis.com/css2?family=Anton&family=Tinos:wght@400;700&display=swap">
<style>
  :root {
    --page-bg: #e9e6e2;
    --band-blue: #15599c;
    --band-blue-dark: #0c4581;
    --headline-blue: #0f5aa6;
    --ink-black: #0b0b0b;
    --paper: #ffffff;
    --swoosh: #e4e6ea;
    --tab-grey: #3b3b3d;
    --tick-blue: #5fb2f0;
    --accent-line: #2a8ee0;
    --white: #ffffff;
  }
  * { box-sizing: border-box; margin: 0; padding: 0; }
  html, body { width: 907px; height: 1200px; overflow: hidden; }
  body { background: var(--page-bg); position: relative; font-family: "Tinos", "Times New Roman", serif; }

  .poster {
    position: absolute; left: 84px; top: 124px; width: 738px; height: 956px;
    background: var(--paper); overflow: hidden;
    box-shadow: 0 6px 18px rgba(0,0,0,.25);
  }

  .header {
    position: absolute; left: 0; top: 0; width: 100%; height: 153px;
    background: linear-gradient(100deg, var(--band-blue-dark), var(--band-blue) 45%, var(--band-blue-dark));
    color: var(--white);
  }
  .brand { position: absolute; left: 21px; top: 38px; color: var(--white); font-weight: 400; text-align: center; width: 290px; }
  .brand-name { font-size: 31px; letter-spacing: .5px; line-height: 1; display: block; }
  .brand-sub { font-size: 17px; letter-spacing: 9px; display: block; margin-top: 8px; }

  .contact { position: absolute; right: 10px; top: 27px; list-style: none; text-align: right; font-size: 15px; line-height: 18.7px; }
  .contact li { display: flex; justify-content: flex-end; align-items: center; gap: 8px; }
  .contact svg { width: 11px; height: 11px; flex: none; }
  .contact .no-icon { margin-right: 19px; }

  .stage {
    position: absolute; left: 0; top: 153px; width: 100%; height: 671px;
    background:
      radial-gradient(ellipse 70% 18% at 30% 35%, var(--swoosh), transparent 70%),
      radial-gradient(ellipse 60% 14% at 75% 55%, var(--swoosh), transparent 70%),
      var(--paper);
  }
  .photo { position: absolute; border-radius: 4px; }
  .photo-man { left: 4px; top: 238px; width: 272px; height: 433px;
    background: linear-gradient(180deg, #d8b49a 0%, #c9997c 35%, #2a2a2e 60%, #1d1d20 100%); }
  .photo-woman { left: 548px; top: 128px; width: 176px; height: 543px;
    background: linear-gradient(180deg, #5a3a2a 0%, #e2c2ac 15%, #1e2238 30%, #1e2238 62%, #dcb9a2 75%, #1a1a1e 100%); }

  .headline { position: absolute; font-family: "Anton", "Impact", sans-serif; line-height: 1; }
  .headline-blue { color: var(--headline-blue); font-size: 140px; left: 0; width: 100%; text-align: center; padding-left: 20px;
    text-shadow: 3px 3px 0 var(--white), 5px 6px 6px rgba(0,0,0,.35); }
  .line-life { top: 50px; }
  .line-short { top: 218px; }
  .headline-black { color: var(--ink-black); font-size: 70px; left: 278px;
    text-shadow: 2px 2px 0 var(--white), 4px 4px 5px rgba(0,0,0,.3); }
  .line-get { top: 485px; }
  .line-divorce { top: 558px; }

  .footer {
    position: absolute; left: 0; top: 824px; width: 100%; height: 132px;
    background: linear-gradient(100deg, var(--band-blue-dark), var(--band-blue) 50%, var(--band-blue-dark));
  }
  .services-tab {
    position: absolute; left: 288px; top: -10px; width: 163px; height: 44px;
    background: var(--tab-grey); color: var(--white); font-size: 26px; text-align: center; line-height: 44px;
  }
  .services-list { position: absolute; top: 42px; list-style: none; color: var(--white); font-size: 16px; line-height: 20.5px; }
  .services-list li { display: flex; align-items: center; gap: 5px; }
  .services-list svg { width: 11px; height: 11px; flex: none; }
  .col-1 { left: 21px; }
  .col-2 { left: 245px; }
  .col-3 { left: 510px; }
  .accent-line { position: absolute; left: 0; bottom: 0; width: 100%; height: 8px; background: var(--accent-line); }
</style>
</head>
<body>
<main class="poster">
  <header class="header">
    <div class="brand">
      <span class="brand-name">MARLOW KEANE</span>
      <span class="brand-sub">LEGAL</span>
    </div>
    <ul class="contact">
      <li>Level 2 /28 Harbour Lane <svg viewBox="0 0 12 12"><path d="M6 1a3.5 3.5 0 0 0-3.5 3.5C2.5 7.5 6 11 6 11s3.5-3.5 3.5-6.5A3.5 3.5 0 0 0 6 1zm0 5a1.5 1.5 0 1 1 0-3 1.5 1.5 0 0 1 0 3z" fill="#fff"/></svg></li>
      <li class="no-icon">Portvale NT 0810, PO Box 4172 Portvale NT 0811</li>
      <li>(08) 5550 1427 <svg viewBox="0 0 12 12"><path d="M3 1l2 2.5-1.2 1.3a7 7 0 0 0 3.4 3.4L8.5 7 11 9l-1.3 2C5.5 11 1 6.5 1 2.3z" fill="#fff"/></svg></li>
      <li>www.marlowkeanelegal.com <svg viewBox="0 0 12 12"><circle cx="6" cy="6" r="5" fill="none" stroke="#fff" stroke-width="1.2"/><path d="M1 6h10M6 1c-2 2.5-2 7.5 0 10M6 1c2 2.5 2 7.5 0 10" fill="none" stroke="#fff" stroke-width="1"/></svg></li>
      <li>office@marlowkeanelegal.com <svg viewBox="0 0 12 12"><rect x="1" y="3" width="10" height="7" fill="none" stroke="#fff" stroke-width="1.2"/><path d="M1 3l5 4 5-4" fill="none" stroke="#fff" stroke-width="1.2"/></svg></li>
    </ul>
  </header>

  <section class="stage">
    <div class="photo photo-man" role="img" aria-label="Photo of a muscular young man in a sleeveless black hoodie and backwards cap, arms crossed"></div>
    <div class="photo photo-woman" role="img" aria-label="Photo of a woman in a navy business suit and high heels, arms crossed"></div>
    <h1 class="headline headline-blue line-life">Life's</h1>
    <p class="headline headline-blue line-short">Short</p>
    <p class="headline headline-black line-get">GET A</p>
    <p class="headline headline-black line-divorce">DIVORCE</p>
  </section>

  <footer class="footer">
    <h2 class="services-tab">SERVICES</h2>
    <ul class="services-list col-1">
      <li><svg viewBox="0 0 12 12"><path d="M1.5 6.5l3 3 6-7" fill="none" stroke="#5fb2f0" stroke-width="2"/></svg>Family Law</li>
      <li><svg viewBox="0 0 12 12"><path d="M1.5 6.5l3 3 6-7" fill="none" stroke="#5fb2f0" stroke-width="2"/></svg>Criminal Law</li>
      <li><svg viewBox="0 0 12 12"><path d="M1.5 6.5l3 3 6-7" fill="none" stroke="#5fb2f0" stroke-width="2"/></svg>Traffic &amp; Drink Driving</li>
    </ul>
    <ul class="services-list col-2">
      <li><svg viewBox="0 0 12 12"><path d="M1.5 6.5l3 3 6-7" fill="none" stroke="#5fb2f0" stroke-width="2"/></svg>Commercial &amp; Property Law</li>
      <li><svg viewBox="0 0 12 12"><path d="M1.5 6.5l3 3 6-7" fill="none" stroke="#5fb2f0" stroke-width="2"/></svg>Conveyancing</li>
      <li><svg viewBox="0 0 12 12"><path d="M1.5 6.5l3 3 6-7" fill="none" stroke="#5fb2f0" stroke-width="2"/></svg>Domestic Violence</li>
    </ul>
    <ul class="services-list col-3">
      <li><svg viewBox="0 0 12 12"><path d="M1.5 6.5l3 3 6-7" fill="none" stroke="#5fb2f0" stroke-width="2"/></svg>General Litigation matters</li>
      <li><svg viewBox="0 0 12 12"><path d="M1.5 6.5l3 3 6-7" fill="none" stroke="#5fb2f0" stroke-width="2"/></svg>Debt Recovery</li>
      <li><svg viewBox="0 0 12 12"><path d="M1.5 6.5l3 3 6-7" fill="none" stroke="#5fb2f0" stroke-width="2"/></svg>Wills &amp; Estates</li>
    </ul>
    <div class="accent-line"></div>
  </footer>
</main>
</body>
</html>
```